Verra needs a new design we have an updated logo and want a high qualitative high end feel

feel and aesthetic should be high qualitative like the packaging in a zuvi or the qualatative weight/feel of an zuvi design. modern, elegant bold.probably just the verra logo on the backone vesion could be blue background white letter ... open to ideas
Target Market(s)
legal, insurance , medical, finance rho 740
Industry/Entity Type
Information Technology
Font styles to use
Serif

```html
<!DOCTYPE html>
<html lang="en">
<head>
<meta charset="utf-8">
<title>Verra Business Cards</title>
<link rel="stylesheet" href="https://fonts.googleapis.com/css2?family=Open+Sans:wght@400;600;700&family=Oswald:wght@500&display=swap">
<style>
  :root {
    --backdrop: #1c1d1f;
    --navy: #172a3c;
    --white: #ffffff;
    --silver: #c8ced5;
    --text-light: #e9eef3;
  }
  * { margin: 0; padding: 0; box-sizing: border-box; }
  html, body {
    width: 1200px; height: 895px; overflow: hidden;
    background: var(--backdrop);
    font-family: "Open Sans", Arial, sans-serif;
  }
  .canvas { position: relative; width: 1200px; height: 895px; }

  .card {
    position: absolute;
    width: 560px; height: 320px;
    overflow: hidden;
    box-shadow: 0 14px 30px rgba(0,0,0,.55);
  }

  /* Back of card */
  .card-back { left: 70px; top: 110px; background: var(--navy); }
  .card-back .brand {
    position: absolute; left: 110px; top: 118px;
    display: flex; align-items: center; gap: 22px;
  }
  .card-back .brand-name {
    font-size: 86px; font-weight: 600; line-height: 1;
    color: var(--silver); letter-spacing: 1px;
  }
  .card-back .brand-tagline {
    font-family: "Oswald", "Arial Narrow", sans-serif;
    font-size: 13px; font-weight: 500; line-height: 1.4;
    color: var(--silver); letter-spacing: 1.5px;
  }
  .card-back .brand-tagline span { display: block; }
  .card-back .brand-tagline span:nth-child(2) { padding-left: 10px; }
  .card-back .brand-tagline span:nth-child(3) { padding-left: 20px; }

  /* Front of card */
  .card-front { left: 570px; top: 470px; background: var(--white); }
  .card-front .wave { position: absolute; inset: 0; width: 100%; height: 100%; }
  .card-front .brand-name {
    position: absolute; right: 48px; top: 34px;
    font-size: 58px; font-weight: 600; line-height: 1;
    color: var(--navy);
  }
  .card-front .address {
    position: absolute; right: 26px; top: 166px;
    text-align: right; color: var(--text-light);
    font-style: normal; font-size: 13px; line-height: 1.45;
  }
  .card-front .person {
    position: absolute; left: 36px; top: 200px; color: var(--white);
  }
  .card-front .person-role { font-size: 13px; line-height: 1.25; }
  .card-front .person-name { font-size: 19px; font-weight: 700; letter-spacing: .5px; line-height: 1.25; }
  .card-front .contact-list {
    position: absolute; left: 36px; top: 254px;
    list-style: none; color: var(--text-light); font-size: 13px;
  }
  .card-front .contact-list li { display: flex; align-items: center; gap: 8px; line-height: 1.45; }
  .card-front .contact-list svg { width: 11px; height: 11px; fill: var(--text-light); flex: none; }
</style>
</head>
<body>
<main class="canvas">

  <section class="card card-back" aria-label="Card back">
    <div class="brand">
      <div class="brand-name">verra</div>
      <div class="brand-tagline">
        <span>DIGITAL</span>
        <span>SYSTEMS</span>
        <span>PARTNERS, LLC</span>
      </div>
    </div>
  </section>

  <section class="card card-front" aria-label="Card front">
    <svg class="wave" viewBox="0 0 560 320" preserveAspectRatio="none" aria-hidden="true">
      <path d="M0 222 C 90 160, 220 175, 330 160 C 440 146, 530 120, 560 70 L 560 320 L 0 320 Z" fill="var(--navy)"/>
      <path d="M40 196 C 150 150, 260 152, 360 140 C 460 128, 535 100, 552 58" fill="none" stroke="var(--navy)" stroke-width="3"/>
      <path d="M200 158 C 280 146, 380 140, 470 120" fill="none" stroke="var(--navy)" stroke-width="1.5"/>
    </svg>

    <div class="brand-name">verra</div>

    <address class="address">
      480 Linden Ave Suite 12<br>
      Marlow, VA 23100
    </address>

    <div class="person">
      <div class="person-role">Founder &amp; CEO</div>
      <div class="person-name">DANIEL HALE</div>
    </div>

    <ul class="contact-list">
      <li>
        <svg viewBox="0 0 24 24" aria-hidden="true"><path d="M6.6 10.8a15 15 0 0 0 6.6 6.6l2.2-2.2a1 1 0 0 1 1-.25 11 11 0 0 0 3.6.6 1 1 0 0 1 1 1V20a1 1 0 0 1-1 1A17 17 0 0 1 3 4a1 1 0 0 1 1-1h3.5a1 1 0 0 1 1 1 11 11 0 0 0 .6 3.6 1 1 0 0 1-.25 1z"/></svg>
        000 000 0000
      </li>
      <li>
        <svg viewBox="0 0 24 24" aria-hidden="true"><path d="M2 5h20v14H2z M2 5l10 8 10-8" stroke="var(--navy)" stroke-width="1.5"/></svg>
        info@verratech.com
      </li>
      <li>
        <svg viewBox="0 0 24 24" aria-hidden="true"><circle cx="12" cy="12" r="10"/><path d="M2 12h20M12 2c3 3 3 17 0 20M12 2c-3 3-3 17 0 20" fill="none" stroke="var(--navy)" stroke-width="1.5"/></svg>
        www.verratech.com
      </li>
    </ul>
  </section>

</main>
</body>
</html>
```